Box design for toddler shoes

Hi,

TASK:
I need a shoe box designed for our rubber soled socks.

DIMENSION:
13.5cmHx12cmWx7.2cmD

​BOX FEATURE:
1. Must include the following information
a) our logo
b) the product name ‘Rubber Soled Socks’
c) Some product key features that could be written on the box include:
- Indoor and outdoor wear
- Soft and flexible sole
- Light weight and comfortable
d) Sock composition and care instructions also needs to be included on the box,
probably quite small. Maybe on the base.

Sock: 80% Cotton 10% Spandex 10% Polyester
Rubber Sole

Care instructions:
Cold Machine Wash or Hand Wash
Do not bleach
Do not tumble dry

Made in China
Distributed by TW Tots
www.twtots.com.au

2. A CUT OUT in the lid so you can see at least part of the shoe/sock pattern design. I am open to different size and shape cut outs, but need the shoes to not be at risk of falling out of the box.

DESIGN KEYPOINTS:
1. I would like a modern classic design. I like the yellow shoe box picture attached, but am happy and open for a different design. This just gives you the idea of the fresh look I like.

2. NO brown craft packaging, but am open to options for other colours.

3. NO picture of the socks on the box design
- the CUT on the lid will allow buyer to see the pattern on the socks. Attached is images of the sample shoe/socks that will be put in the boxes and how they will be packaged in the rectangle box. There are many different designs/colour. All will need to be packaged in the same box.

4. I'd love to see what the box would look like as it sits on the shelf, but also need the flat lay design ready for printing.

Please let me know if you have any questions to help with your design.

I can't wait to see your design.

Thanks,
Maya

Industry/Entity Type

Baby/kids

Font styles to use
Sans Serif
Other font styles liked:
• More modern version of Sans Serif

Requirements
Must have
• Cut out in the top of the box so you can see part of the sock to know which design is packaged inside.
Should not have
• Bubble font

```html
<!DOCTYPE html>
<html lang="en">
<head>
<meta charset="utf-8">
<title>Rubber Soled Socks – Box Dielines</title>
<link rel="stylesheet" href="https://fonts.googleapis.com/css2?family=Poppins:wght@400;500;600;700;800&display=swap">
<style>
  :root{
    --bg:#e4e4e4;
    --red:#ed2630;
    --white:#ffffff;
    --grey:#7a7a7a;
    --ink:#222222;
    --window:#c4c4c4;
  }
  html,body{margin:0;padding:0;overflow:hidden;}
  body{width:834px;height:1200px;background:var(--bg);font-family:'Poppins',sans-serif;display:flex;align-items:center;justify-content:center;}
  .dielines{display:block;width:834px;height:auto;}
  .panel-white{fill:var(--white);stroke:#9a9a9a;stroke-width:1;}
  .panel-red{fill:var(--red);stroke:#b81a22;stroke-width:1;}
  .title-main{font-weight:800;letter-spacing:-1px;}
  .title-sub{font-weight:800;letter-spacing:-0.5px;}
  .fill-red{fill:var(--red);}
  .fill-grey{fill:var(--grey);}
  .fill-white{fill:var(--white);}
  .fill-ink{fill:var(--ink);}
  .care-head{font-weight:700;font-size:11px;}
  .care-item{font-weight:400;font-size:9px;}
  .url{font-weight:400;font-size:12px;}
  .small-print{font-weight:400;font-size:5.5px;}
  .brand-name{font-weight:400;}
  .feature{font-weight:400;font-size:11px;}
  .icon-line{fill:none;stroke:var(--ink);stroke-width:0.8;}
</style>
</head>
<body>
<svg class="dielines" viewBox="70 1290 1480 790" xmlns="http://www.w3.org/2000/svg" aria-label="Flat print layouts for box base and lid">
  <defs>
    <filter id="panelShadow" x="-5%" y="-5%" width="110%" height="110%">
      <feDropShadow dx="2" dy="3" stdDeviation="2" flood-opacity="0.25"/>
    </filter>
  </defs>

  <!-- Box base layout -->
  <g class="base-layout" filter="url(#panelShadow)">
    <rect class="panel-white" x="295" y="1310" width="385" height="205"/>
    <rect class="panel-red" x="88" y="1515" width="207" height="343"/>
    <rect class="panel-red" x="295" y="1515" width="385" height="343"/>
    <rect class="panel-red" x="680" y="1515" width="206" height="343"/>
    <rect class="panel-white" x="295" y="1858" width="385" height="205"/>
  </g>

  <g class="base-end-top">
    <text class="title-main fill-red" x="487" y="1387" font-size="44" text-anchor="middle">RUBBER</text>
    <text class="title-sub fill-grey" x="487" y="1413" font-size="25" text-anchor="middle">SOLED SOCKS</text>
    <text class="care-head fill-ink" x="326" y="1437">Care instructions</text>
    <g class="care-list">
      <circle class="icon-line" cx="329" cy="1452" r="4.5"/>
      <text class="care-item fill-ink" x="338" y="1455">Cold Machine Wash or Hand Wash</text>
      <circle class="icon-line" cx="329" cy="1467" r="4.5"/>
      <path class="icon-line" d="M326 1470 L329 1464 L332 1470 Z"/>
      <text class="care-item fill-ink" x="338" y="1470">Do not bleach</text>
      <circle class="icon-line" cx="329" cy="1482" r="4.5"/>
      <rect class="icon-line" x="326.5" y="1479.5" width="5" height="5"/>
      <text class="care-item fill-ink" x="338" y="1485">Do not tumble dry</text>
    </g>
    <text class="url fill-ink" x="583" y="1480" text-anchor="middle">www.<tspan class="fill-red">twtots</tspan>.com.au</text>
    <text class="small-print fill-ink" x="583" y="1494" text-anchor="middle">Sock: 80% Cotton | 10% Spandex | 10% Polyester | Rubber Sole</text>
  </g>

  <g class="base-side-left" transform="rotate(-90 190 1686)">
    <text class="title-main fill-white" x="190" y="1682" font-size="50" text-anchor="middle">RUBBER</text>
    <text class="title-sub fill-white" x="190" y="1710" font-size="27" text-anchor="middle">SOLED SOCKS</text>
  </g>

  <text class="url fill-white" x="487" y="1696" text-anchor="middle">www.twtots.com.au</text>

  <g class="base-side-right" transform="rotate(90 783 1686)">
    <text class="title-main fill-white" x="783" y="1682" font-size="50" text-anchor="middle">RUBBER</text>
    <text class="title-sub fill-white" x="783" y="1710" font-size="27" text-anchor="middle">SOLED SOCKS</text>
  </g>

  <g class="base-end-bottom" transform="rotate(180 487 1960)">
    <text class="title-main fill-red" x="487" y="1962" font-size="44" text-anchor="middle">RUBBER</text>
    <text class="title-sub fill-grey" x="487" y="1988" font-size="25" text-anchor="middle">SOLED SOCKS</text>
    <text class="care-item fill-ink" x="317" y="2010">Made in China</text>
    <text class="care-item fill-ink" x="317" y="2021" font-weight="700">Distributed by TW Tots</text>
    <text class="care-item fill-ink" x="317" y="2032">www.twtots.com.au</text>
    <text class="brand-name fill-ink" x="593" y="2025" font-size="17" text-anchor="middle">Little Rowan</text>
  </g>

  <!-- Box lid layout -->
  <g class="lid-layout" filter="url(#panelShadow)">
    <rect class="panel-white" x="1043" y="1407" width="385" height="108"/>
    <rect class="panel-white" x="934" y="1515" width="109" height="343"/>
    <rect class="panel-red" x="1043" y="1515" width="385" height="343"/>
    <rect class="panel-white" x="1428" y="1515" width="109" height="343"/>
    <rect class="panel-white" x="1043" y="1858" width="385" height="107"/>
  </g>

  <text class="url fill-ink" x="1236" y="1460" text-anchor="middle" transform="rotate(180 1236 1456)">www.<tspan class="fill-red">twtots</tspan>.com.au</text>
  <text class="url fill-ink" x="988" y="1690" text-anchor="middle" transform="rotate(90 988 1686)" font-size="11">www.<tspan class="fill-red">twtots</tspan>.com.au</text>
  <text class="url fill-ink" x="1484" y="1690" text-anchor="middle" transform="rotate(-90 1484 1686)" font-size="11">www.<tspan class="fill-red">twtots</tspan>.com.au</text>
  <text class="url fill-ink" x="1236" y="1917" text-anchor="middle">www.<tspan class="fill-red">twtots</tspan>.com.au</text>

  <g class="lid-top">
    <text class="brand-name fill-white" x="1243" y="1594" font-size="30" text-anchor="middle">Little Rowan</text>
    <text class="title-main fill-white" x="1173" y="1696" font-size="46" text-anchor="middle">RUBBER</text>
    <text class="title-sub fill-white" x="1173" y="1723" font-size="25" text-anchor="middle">SOLED SOCKS</text>
    <rect class="window-cutout" x="1283" y="1640" width="124" height="92" rx="6" fill="var(--window)" stroke="#8a8a8a" stroke-width="1"/>

    <g class="feature-list">
      <rect x="1085" y="1764" width="14" height="14" rx="2" class="fill-white"/>
      <text class="feature fill-white" x="1104" y="1770">Indoor and</text>
      <text class="feature fill-white" x="1104" y="1781">outdoor wear</text>
      <line x1="1182" y1="1760" x2="1182" y2="1786" stroke="var(--white)" stroke-width="1"/>
      <rect x="1192" y="1764" width="14" height="14" rx="2" class="fill-white"/>
      <text class="feature fill-white" x="1213" y="1770">Soft and</text>
      <text class="feature fill-white" x="1213" y="1781">flexible sole</text>
      <line x1="1282" y1="1760" x2="1282" y2="1786" stroke="var(--white)" stroke-width="1"/>
      <rect x="1291" y="1764" width="14" height="14" rx="2" class="fill-white"/>
      <text class="feature fill-white" x="1311" y="1770">Light weight</text>
      <text class="feature fill-white" x="1311" y="1781">and comfortable</text>
    </g>
    <text class="url fill-white" x="1236" y="1825" text-anchor="middle">www.twtots.com.au</text>
  </g>
</svg>
</body>
</html>
```